Clean Plinth Ads Banner Design For A Finance Company

Hi,
We're a UK based finance company and are looking for new banner ads to use on the Plinth Display Network.
We want the end product to stand out by using strong, minimal design - ideally starting from a dark theme, although I'm open to ideas.
The copy should read:
'Fast Bridging Loans From 0.39% PM'
Once we have these designs agreed, we are looking to replicate them for other products, changing only the text on each ad - for example, 'commercial mortgage service you can rely on' or 'development finance service you can rely on'.
The colours used on our website are the following:
Black - #040303
Orange - #f79124
White - #ffffff
Grey - #ffffff
Example ads that I like - https://www.brimcastle.com/wp-content/uploads/2021/07/plinth-display-ads-example-2-final.png.webp
2 - https://quendrahub.com/wp-content/uploads/2020/03/fbdd56ba3bd16c7a8debb13a411de786.jpg

```html
<!DOCTYPE html>
<html lang="en">
<head>
<meta charset="utf-8">
<title>Ledra Finance – Fast Bridging Loans Banner</title>
<link rel="stylesheet" href="https://fonts.googleapis.com/css2?family=Montserrat:wght@600;700;800&display=swap">
<style>
  :root {
    --brand-black: #040303;
    --brand-orange: #f79124;
    --brand-white: #ffffff;
    --page-grey: #f0f0f2;
    --photo-dark: #1c1a1c;
    --photo-pink: #d98a93;
    --photo-blue: #8fb8d0;
    --photo-glow: #b86a1c;
  }
  * { margin: 0; padding: 0; box-sizing: border-box; }
  html, body {
    width: 1200px;
    height: 330px;
    overflow: hidden;
    background: var(--page-grey);
    font-family: "Montserrat", Arial, sans-serif;
  }
  .stage {
    position: relative;
    width: 1200px;
    height: 330px;
  }
  .banner {
    position: absolute;
    left: 32px;
    top: 41px;
    width: 1136px;
    height: 247px;
    background: var(--brand-black);
    overflow: hidden;
  }
  .banner-shapes {
    position: absolute;
    left: 0;
    top: 0;
    width: 340px;
    height: 247px;
  }
  .headline {
    position: absolute;
    left: 395px;
    top: 60px;
    color: var(--brand-white);
    line-height: 1;
  }
  .headline-lead {
    display: block;
    font-size: 35.5px;
    font-weight: 700;
    letter-spacing: 0.2px;
    white-space: nowrap;
  }
  .headline-rate {
    display: block;
    margin-top: 4px;
    margin-left: -4px;
    font-size: 106px;
    font-weight: 700;
    color: var(--brand-orange);
    letter-spacing: -1px;
    white-space: nowrap;
  }
  .brand {
    position: absolute;
    right: 28px;
    top: 12px;
    text-align: right;
    color: var(--brand-orange);
    font-weight: 700;
    line-height: 1;
  }
  .brand-name {
    display: block;
    font-size: 34px;
    letter-spacing: -0.5px;
  }
  .brand-descriptor {
    display: block;
    margin-top: 4px;
    font-size: 9.5px;
    letter-spacing: 0.3px;
  }
</style>
</head>
<body>
<div class="stage">
  <section class="banner" aria-label="Ledra Finance bridging loans advert">
    <svg class="banner-shapes" viewBox="0 0 340 247" xmlns="http://www.w3.org/2000/svg">
      <defs>
        <radialGradient id="photo-tone" cx="0.45" cy="0.45" r="0.7">
          <stop offset="0" stop-color="var(--photo-blue)"/>
          <stop offset="0.35" stop-color="var(--photo-pink)"/>
          <stop offset="0.75" stop-color="var(--photo-glow)"/>
          <stop offset="1" stop-color="var(--photo-dark)"/>
        </radialGradient>
      </defs>
      <path class="accent-top" fill="var(--brand-orange)"
            d="M200,0 L275,0 C292,25 288,58 262,82 C262,55 250,18 210,0 Z"/>
      <path class="accent-corner" fill="var(--brand-orange)"
            d="M35,0 L52,0 C44,4 38,6 35,6 Z"/>
      <path class="accent-bottom" fill="var(--brand-orange)"
            d="M0,120 C45,150 80,200 100,247 L0,247 Z"/>
      <path class="photo-area" role="img"
            aria-label="Photo: pink piggy bank wearing a face mask beside stacks of coins"
            fill="url(#photo-tone)"
            d="M0,0 L210,0 C250,20 258,60 262,95 C268,150 330,165 332,210 C334,238 305,247 282,247 L88,247 C62,200 32,168 0,152 Z"/>
    </svg>

    <h1 class="headline">
      <span class="headline-lead">FAST BRIDGING LOANS FROM</span>
      <span class="headline-rate">0.39% PM</span>
    </h1>

    <div class="brand">
      <span class="brand-name">Ledra</span>
      <span class="brand-descriptor">Finance Limited</span>
    </div>
  </section>
</div>
</body>
</html>
```